Company Website for Vortel Insight, an open source data analytics company focused on relationship and li

I need a company/brand website for our new startup, Vortel Insight LLC. We are a company focused on using life pattern analysis techniques, looking at relationships and how relationships, attributes, and activity cluster to infer aggregate information about individuals and groups. Our focus is on improving the digital advertising market.

We have a company logo which I will upload shortly.

Target Market(s)

Digital Advertising

Number of Pages Required

3 page

Font styles to use
Sans Serif

Requirements
Must have
• An main page, about us, contact page.
Nice to have
• Vortel Insight relies on state of the art analytics applied to a the digital marketing space. While it is heavy in science, we also understand the art of influence. The website should have a scientific edge but also a flair that illustrates our focus on applying the hard science and analytics to influencing the behavior of people.

```html
<!DOCTYPE html>
<html lang="en">
<head>
<meta charset="utf-8">
<title>Vortel Insight</title>
<link rel="stylesheet" href="https://fonts.googleapis.com/css2?family=Open+Sans:wght@300;400;600;700;800&display=swap">
<style>
:root{
  --blue:#1f93da;
  --blue-dark:#1a7fc4;
  --orange:#f07d1a;
  --grey-text:#666;
  --heading:#333;
  --lavender:#e7e6ef;
  --dark:#2c2c2c;
  --darker:#222;
  --white:#fff;
  --feature-grey:#7d7472;
}
*{margin:0;padding:0;box-sizing:border-box}
html,body{width:1200px;height:2885px;overflow:hidden}
body{font-family:"Open Sans",Arial,sans-serif;color:var(--grey-text);background:var(--white);position:relative}
section,header,footer{position:absolute;left:0;width:1200px}
.abs{position:absolute}
.center{left:0;width:1200px;text-align:center}

/* header */
.site-header{top:0;height:115px;background:var(--white)}
.brand{left:100px;top:38px;display:flex;align-items:center;gap:10px;font-size:26px;font-weight:700;color:var(--blue)}
.brand-dot{width:16px;height:16px;border-radius:50%;background:var(--orange)}
.main-nav{top:46px;left:0;width:1200px;font-size:14px;color:#333}
.main-nav a{position:absolute;text-decoration:none;color:inherit;white-space:nowrap}
.main-nav a.active{color:var(--orange)}
.main-nav a.active::after{content:"";position:absolute;left:0;right:0;top:28px;height:2px;background:var(--orange)}

/* hero */
.hero{top:115px;height:580px;overflow:hidden}
.hero-photo{position:absolute;inset:0;background:linear-gradient(120deg,#5a6470 0%,#a7afb8 35%,#c9cdd2 55%,#8a939c 80%,#4e5863 100%)}
.hero-title{top:130px;font-size:112px;font-weight:800;color:var(--white);letter-spacing:3px;line-height:1}
.hero-sub{top:254px;font-size:14px;color:var(--white)}
.btn{display:block;background:var(--blue);color:var(--white);text-align:center;font-weight:600}
.hero-btn{left:508px;top:300px;width:182px;height:52px;line-height:52px;font-size:18px}
.hero-arrow{top:255px;width:44px;height:44px}
.hero-curve{left:0;bottom:0;width:1200px;height:70px}

/* shared headings */
.section-title{font-size:38px;font-weight:300;line-height:1}
.rule{position:absolute;left:550px;width:100px;height:3px;background:var(--orange)}

/* welcome */
.welcome{top:695px;height:368px;background:#f8f8f8}
.welcome .section-title{top:31px;color:var(--heading)}
.welcome .rule{top:77px}
.welcome p{position:absolute;left:124px;width:952px;text-align:center;font-size:14px;line-height:27px;color:var(--grey-text)}

/* services */
.services{top:1063px;height:690px;background:linear-gradient(180deg,var(--blue) 0%,var(--blue-dark) 100%)}
.services .section-title{top:72px;color:var(--white)}
.services .rule{top:118px;background:var(--white)}
.service{position:absolute;width:300px;text-align:center;color:var(--white)}
.service-ring{width:144px;height:144px;margin:0 auto;border:1.5px solid rgba(255,255,255,.75);border-radius:50%;display:flex;align-items:center;justify-content:center}
.service-name{margin-top:22px;font-size:14px;font-weight:700}

/* features */
.features{top:1753px;height:587px;background:linear-gradient(180deg,#ebeaf2,#e1e0ea)}
.features .section-title{top:71px;color:var(--heading)}
.features .rule{top:114px}
.features .intro{position:absolute;left:130px;width:940px;top:143px;text-align:center;font-size:14px;line-height:27px}
.feature{position:absolute;top:257px;width:280px;text-align:center}
.feature-icon{width:116px;height:116px;margin:0 auto;border-radius:50%;display:flex;align-items:center;justify-content:center}
.feature h3{margin-top:10px;font-size:22px;font-weight:600;line-height:30px}
.feature p{margin-top:6px;font-size:13px;line-height:21px;color:#555}
.integrate .feature-icon{background:var(--feature-grey)} .integrate h3{color:var(--feature-grey)}
.analyze .feature-icon{background:var(--orange)} .analyze h3{color:var(--orange)}
.visualize .feature-icon{background:var(--blue)} .visualize h3{color:var(--blue)}

/* contact */
.contact{top:2340px;height:475px;background:var(--dark);color:var(--white)}
.contact .section-title{top:60px}
.contact .rule{top:106px}
.contact .lead{top:121px;font-size:13px;color:#ddd}
.field{position:absolute;border:1px solid #5a5a5a;font-size:14px;color:#eee;padding:12px 16px}
.submit{left:496px;top:352px;width:208px;height:54px;line-height:54px;font-size:20px;font-weight:400;letter-spacing:.5px}

.site-footer{top:2815px;height:70px;background:var(--darker);text-align:center;line-height:70px;font-size:12px;color:#888}
</style>
</head>
<body>

<header class="site-header">
  <div class="abs brand"><span class="brand-dot"></span>Vortel Insight</div>
  <nav class="abs main-nav">
    <a class="active" style="left:511px">HOME</a>
    <a style="left:607px">ABOUT US</a>
    <a style="left:727px">OUR SERVICES</a>
    <a style="left:869px">OUR FEATURES</a>
    <a style="left:1020px">CONTACT US</a>
  </nav>
</header>

<section class="hero">
  <div class="hero-photo" role="img" aria-label="Photo of a hand working over a tablet with data charts and analytics overlays"></div>
  <h1 class="abs center hero-title">VORTEL INSIGHT</h1>
  <p class="abs center hero-sub">We are an open source data analytics company focused on relationship and lifestyle behaviors.</p>
  <a class="abs btn hero-btn">LEARN MORE</a>
  <svg class="abs hero-arrow" style="left:26px" viewBox="0 0 44 44"><path d="M26 10 L14 22 L26 34" fill="none" stroke="#fff" stroke-width="1.5"/></svg>
  <svg class="abs hero-arrow" style="left:1120px" viewBox="0 0 44 44"><circle cx="22" cy="22" r="22" fill="rgba(0,0,0,.25)"/><path d="M18 10 L30 22 L18 34" fill="none" stroke="#fff" stroke-width="1.5"/></svg>
  <svg class="abs hero-curve" viewBox="0 0 1200 70" preserveAspectRatio="none"><path d="M0 70 Q600 -55 1200 70 Z" fill="#f8f8f8"/></svg>
</section>

<section class="welcome">
  <h2 class="abs center section-title">WELCOME TO VORTEL INSIGHT</h2>
  <span class="rule"></span>
  <p style="top:104px">Sed ut perspiciatis unde omnis iste natus error sit voluptatem accusantium doloremque laudantium, totam rem aperiam, eaque ipsa quae ab illo inventore veritatis et quasi architecto beatae vitae dicta sunt explicabo. Nemo enim ipsam voluptatem quia voluptas sit aspernatur aut odit aut fugit, sed quia consequuntur magni dolores eos qui ratione voluptatem sequi nesciunt.</p>
  <p style="top:216px">Neque porro quisquam est, qui dolorem ipsum quia dolor sit amet, consectetur, adipisci velit, sed quia non numquam eius modi tempora incidunt ut labore et dolore magnam aliquam quaerat voluptatem.</p>
</section>

<section class="services">
  <h2 class="abs center section-title">OUR SERVICES</h2>
  <span class="rule"></span>

  <div class="service" style="left:108px;top:167px">
    <div class="service-ring"><svg width="70" height="60" viewBox="0 0 70 60" fill="none" stroke="#fff" stroke-width="3"><rect x="4" y="4" width="62" height="40"/><path d="M35 44v8M22 54h26"/><path d="M18 36v-10M28 36v-16M38 36v-12M48 36v-20" stroke-width="5"/></svg></div>
    <div class="service-name">Voluptatem Accusantium</div>
  </div>
  <div class="service" style="left:448px;top:167px">
    <div class="service-ring"><svg width="56" height="66" viewBox="0 0 56 66" fill="none" stroke="#fff" stroke-width="3"><rect x="18" y="3" width="34" height="44"/><rect x="11" y="10" width="34" height="44" fill="var(--blue)"/><rect x="4" y="18" width="34" height="44" fill="var(--blue)"/><path d="M11 30h20M11 38h20M11 46h20M11 54h14"/></svg></div>
    <div class="service-name">Doloremque Laudantium</div>
  </div>
  <div class="service" style="left:808px;top:167px">
    <div class="service-ring"></div>
    <div class="service-name">Totam Rem Aperiam</div>
  </div>

  <div class="service" style="left:108px;top:405px">
    <div class="service-ring"><svg width="70" height="70" viewBox="0 0 70 70" fill="#fff"><path d="M10 24 L35 12 L60 24 L35 36Z"/><path d="M8 28 L33 40 L33 66 L8 54Z"/><path d="M37 40 L62 28 L62 54 L37 66Z"/><path d="M48 4 L66 4 L60 18 L42 18Z"/></svg></div>
    <div class="service-name">Magnam Aliquam</div>
  </div>
  <div class="service" style="left:448px;top:405px">
    <div class="service-ring"><svg width="70" height="70" viewBox="0 0 70 70" fill="none" stroke="#fff" stroke-width="3"><path d="M4 6h62"/><rect x="8" y="6" width="54" height="34"/><path d="M14 30 L24 20 L32 28 L42 16 L54 24"/><path d="M35 40v26M24 50 L35 40 L46 50"/></svg></div>
    <div class="service-name">Architecto Beatae</div>
  </div>
  <div class="service" style="left:808px;top:405px">
    <div class="service-ring"><svg width="70" height="60" viewBox="0 0 70 60" fill="none" stroke="#fff" stroke-width="3"><rect x="14" y="6" width="52" height="32"/><path d="M20 30 L30 22 L38 28 L50 16 L58 22"/><path d="M40 38v18M30 56h20"/></svg></div>
    <div class="service-name">Inventore Veritatis</div>
  </div>
</section>

<section class="features">
  <h2 class="abs center section-title">OUR FEATURES</h2>
  <span class="rule"></span>
  <p class="intro">At vero eos et accusamus et iusto odio dignissimos ducimus qui blanditiis praesentium voluptatum deleniti atque corrupti quos dolores et quas molestias excepturi sint occaecati cupiditate non provident.</p>

  <div class="feature integrate" style="left:93px">
    <div class="feature-icon"><svg width="72" height="56" viewBox="0 0 72 56" fill="none" stroke="#fff" stroke-width="3"><circle cx="26" cy="34" r="9"/><path d="M26 16v6M26 46v6M8 34h6M38 34h6M13 21l4 4M35 43l4 4M13 47l4-4M35 25l4-4"/><circle cx="54" cy="16" r="6"/><path d="M54 4v4M54 24v4M42 16h4M62 16h4M46 8l3 3M59 21l3 3M46 24l3-3M59 11l3-3"/></svg></div>
    <h3>INTEGRATE</h3>
    <p>Quis autem vel eum iure reprehenderit qui in ea voluptate velit esse quam nihil molestiae consequatur vel illum qui dolorem</p>
  </div>
  <div class="feature analyze" style="left:460px">
    <div class="feature-icon"><svg width="64" height="64" viewBox="0 0 64 64" fill="none" stroke="#fff" stroke-width="3.5"><circle cx="36" cy="28" r="18"/><path d="M23 41 L8 56"/><path d="M29 34v-6M35 34v-12M41 34v-9" stroke-width="3"/></svg></div>
    <h3>ANALYZE</h3>
    <p>But I must explain to you how all this mistaken idea of denouncing pleasure and praising pain was born and I will give you a complete</p>
  </div>
  <div class="feature visualize" style="left:823px">
    <div class="feature-icon"><svg width="64" height="60" viewBox="0 0 64 60" fill="#fff"><path d="M18 6 A14 14 0 1 0 32 20 L18 20Z"/><path d="M22 2 A14 14 0 0 1 36 16 L22 16Z"/><rect x="22" y="42" width="7" height="14"/><rect x="33" y="34" width="7" height="22"/><rect x="44" y="26" width="7" height="30"/><rect x="55" y="18" width="7" height="38"/></svg></div>
    <h3>VISUALIZE</h3>
    <p>Nam libero tempore, cum soluta nobis est eligendi optio cumque nihil impedit quo minus id quod maxime placeat facere possimus</p>
  </div>
</section>

<section class="contact">
  <h2 class="abs center section-title">CONTACT US</h2>
  <span class="rule"></span>
  <p class="abs center lead">Customers to contact us with following genral enquiries</p>
  <div class="field" style="left:100px;top:171px;width:317px;height:43px">Name</div>
  <div class="field" style="left:441px;top:171px;width:317px;height:43px">Address</div>
  <div class="field" style="left:783px;top:171px;width:317px;height:43px">Email</div>
  <div class="field" style="left:100px;top:237px;width:1000px;height:72px">Comments</div>
  <a class="abs btn submit">SUBMIT NOW !</a>
</section>

<footer class="site-footer">© 2018 Vortel Insight.&nbsp; All right reserved . Term of Use</footer>

</body>
</html>
```